SNACKS packaging uplift

We need to revamp the current popcorn design to a new more elegant , more premium and cleaner design. The new design should have allow the consumer to immediatly relate the new pack to the old design, and not think its a totally new brand. feel free to update the logo, product shots, but we would like to maintain the WHITE identity somehow.

```html
<!DOCTYPE html>
<html lang="en">
<head>
<meta charset="utf-8">
<title>Kerno Nacho Cheese Popcorn – Pack Front</title>
<link rel="stylesheet" href="https://fonts.googleapis.com/css2?family=Patrick+Hand&family=Cairo:wght@500;600&display=swap">
<style>
  :root {
    --cheese: #f6b81c;
    --cheese-deep: #eaa511;
    --cheese-soft: #f9cd55;
    --cheese-light: #fbe27a;
    --pack-white: #f7f7f7;
    --ink: #1d1d1d;
    --popcorn: #f1ece1;
    --page: #ffffff;
  }
  * { box-sizing: border-box; margin: 0; padding: 0; }
  html, body { width: 876px; height: 1200px; overflow: hidden; background: var(--page); }
  .pack {
    position: relative;
    width: 876px;
    height: 1200px;
    background: var(--pack-white);
    overflow: hidden;
    font-family: "Patrick Hand", cursive;
    color: var(--ink);
  }
  .band { position: absolute; left: 0; width: 876px; }
  .band--top { top: 0; height: 230px; }
  .band--bottom { bottom: 0; height: 240px; }
  .band svg { display: block; width: 100%; height: 100%; }

  .badge {
    position: absolute;
    left: 128px; top: 234px;
    width: 122px; height: 94px;
  }
  .badge svg { position: absolute; inset: 0; }
  .badge__text {
    position: absolute; left: 6px; right: 6px; top: 8px; height: 64px;
    display: flex; align-items: center; justify-content: center;
    text-align: center; font-size: 24px; line-height: 1.05;
    transform: rotate(-5deg);
  }

  .brand {
    position: absolute;
    left: 0; right: 0; top: 300px;
    display: flex; justify-content: center; align-items: center; gap: 12px;
  }
  .brand__name {
    font-size: 150px; line-height: 1; color: var(--cheese);
    letter-spacing: 2px;
  }
  .brand__mark {
    width: 22px; height: 22px; border-radius: 50%;
    background: var(--cheese);
  }
  .brand__arabic {
    position: absolute; left: 0; right: 0; top: 458px;
    text-align: center; font-family: "Cairo", sans-serif; font-weight: 600;
    font-size: 22px; line-height: 1.2; color: var(--ink);
  }

  .flavour {
    position: absolute; left: 0; right: 0; top: 510px;
    text-align: center;
  }
  .flavour__ar { font-family: "Cairo", sans-serif; font-weight: 500; font-size: 18px; line-height: 1.3; }
  .flavour__en { font-size: 22px; line-height: 1.3; letter-spacing: 1.5px; }

  .product-shot {
    position: absolute; left: 134px; top: 630px;
    width: 590px; height: 255px;
    border-radius: 40px;
    background: linear-gradient(90deg, var(--popcorn) 0%, #f4ead2 32%, var(--cheese-light) 58%, #f8d02a 100%);
  }

  .doodles { position: absolute; left: 0; top: 0; }
</style>
</head>
<body>
<main class="pack">

  <div class="band band--top" role="img" aria-label="Cheese yellow band with wavy stripes and a hand-drawn snack and cheese doodle pattern">
    <svg viewBox="0 0 876 230" preserveAspectRatio="none">
      <path fill="var(--cheese)" d="M0 0H876V216L828 166L780 216L732 166L684 216L636 166L588 216L540 166L492 216L444 166L396 216L348 166L300 216L252 166L204 216L156 166L108 216L60 166L12 216L0 204Z"/>
      <path fill="var(--cheese-soft)" opacity=".5" d="M0 60C150 20 260 110 440 70S720 30 876 80V120C720 80 600 140 440 110S150 70 0 110Z"/>
    </svg>
  </div>

  <div class="badge">
    <svg viewBox="0 0 122 94">
      <path d="M10 4H110Q118 4 118 12V66Q118 74 110 74H104L106 92L88 74H12Q4 74 4 66V12Q4 4 10 4Z" fill="var(--cheese)" stroke="var(--ink)" stroke-width="2.5"/>
    </svg>
    <p class="badge__text">Air<br>Popped!</p>
  </div>

  <div class="brand">
    <span class="brand__name">KERNO</span>
    <span class="brand__mark"></span>
  </div>
  <p class="brand__arabic" lang="ar" dir="rtl">كيرنو</p>

  <div class="flavour">
    <p class="flavour__ar" lang="ar" dir="rtl">فشار بطعم الجبنة الناتشوز</p>
    <p class="flavour__en">Nacho Cheese flavored popcorn</p>
  </div>

  <div class="product-shot" role="img" aria-label="Product shot of popped popcorn kernels beside a wedge of yellow cheese"></div>

  <svg class="doodles" width="876" height="1200" viewBox="0 0 876 1200" aria-hidden="true">
    <g fill="none" stroke="var(--ink)" stroke-width="3" stroke-linecap="round">
      <path d="M170 576C160 552 182 530 180 506"/>
      <path d="M712 508C722 484 700 462 698 440"/>
      <path d="M664 974C654 950 676 928 674 904"/>
    </g>
    <g fill="var(--cheese)" stroke="var(--ink)" stroke-width="2" stroke-linejoin="round">
      <path d="M172 510L190 494L188 518Z"/>
      <path d="M706 444L690 428L690 452Z"/>
      <path d="M666 908L684 892L682 916Z"/>
      <circle cx="249" cy="560" r="5"/>
      <circle cx="634" cy="507" r="5"/>
      <circle cx="596" cy="612" r="8"/>
      <circle cx="112" cy="640" r="8"/>
      <circle cx="748" cy="748" r="8"/>
      <circle cx="760" cy="858" r="5"/>
      <circle cx="736" cy="590" r="7"/>
    </g>
  </svg>

  <div class="band band--bottom" role="img" aria-label="Cheese yellow band with a hand-drawn doodle pattern of snacks, cheese and TV sets">
    <svg viewBox="0 0 876 240" preserveAspectRatio="none">
      <path fill="var(--cheese)" d="M0 50L48 0L96 50L144 0L192 50L240 0L288 50L336 0L384 50L432 0L480 50L528 0L576 50L624 0L672 50L720 0L768 50L816 0L864 50L876 38V240H0Z"/>
      <path fill="var(--cheese-deep)" opacity=".35" d="M0 150C200 120 360 190 560 160S800 140 876 160V240H0Z"/>
    </svg>
  </div>

</main>
</body>
</html>
```